Probation office requires Colourful A3 Poster to Celebrate our Success in previous year

We require a colourfull A3 Poster to promote our Success in the previous year within our Probation area. The Text we have in this poster (attached document) needs to stand out as much as possible on the poster so shadows and any other way of distinguishing text on the poster should be encouraged.
The theme of the poster is Success and celebration so any images in the poster should reflect this (example balloons, streamers, fireworks).
I have attached to this design the text which we require in the poster and also our company logo which we would require in the poster (ideally in the bottom right corner).
Many thanks for looking at this project

```html
<!DOCTYPE html>
<html lang="en">
<head>
<meta charset="utf-8">
<title>We're Exceptional – Ashbrook Probation</title>
<link href="https://fonts.googleapis.com/css2?family=Cabin+Sketch:wght@400;700&family=Zilla+Slab:wght@300;400;600&display=swap" rel="stylesheet">
<style>
  :root {
    --sky-top: #5b5ea6;
    --sky-mid: #6a6fb4;
    --sky-low: #8a8ec8;
    --text: #f4f2fa;
    --brand: #7b3f98;
    --balloon-blue: #6fa0e0;
    --balloon-pink: #b868b8;
  }
  * { margin: 0; padding: 0; box-sizing: border-box; }
  html, body { width: 848px; height: 1200px; overflow: hidden; background: var(--sky-top); }
  .poster {
    position: relative;
    width: 848px;
    height: 1200px;
    overflow: hidden;
    color: var(--text);
    font-family: "Zilla Slab", Georgia, serif;
    font-weight: 300;
    text-transform: uppercase;
    text-align: center;
    text-shadow: 0 1px 2px rgba(40, 30, 90, 0.35);
  }
  .sky {
    position: absolute;
    inset: 0;
    background:
      radial-gradient(ellipse 420px 260px at 640px 1000px, rgba(214, 196, 236, 0.85), transparent 70%),
      radial-gradient(ellipse 360px 200px at 220px 1120px, rgba(190, 170, 222, 0.7), transparent 70%),
      radial-gradient(ellipse 300px 160px at 760px 780px, rgba(200, 184, 230, 0.55), transparent 70%),
      radial-gradient(ellipse 500px 300px at 430px 640px, rgba(150, 160, 215, 0.45), transparent 70%),
      linear-gradient(180deg, var(--sky-top) 0%, var(--sky-mid) 45%, var(--sky-low) 100%);
  }
  .brand {
    position: absolute;
    left: 26px;
    top: 22px;
    width: 90px;
    display: flex;
    flex-direction: column;
    align-items: center;
    gap: 8px;
  }
  .brand-square { width: 90px; height: 90px; background: var(--brand); }
  .brand-name {
    font-weight: 600;
    font-size: 12px;
    line-height: 1.1;
    color: var(--text);
    text-shadow: none;
  }
  .balloons {
    position: absolute;
    left: 650px;
    top: 30px;
    width: 162px;
    height: 158px;
    border-radius: 50% 50% 45% 45%;
    background: radial-gradient(circle at 40% 35%, var(--balloon-blue), var(--balloon-pink) 60%, rgba(184, 104, 184, 0) 72%);
  }
  .headline {
    position: absolute;
    left: 0;
    right: 0;
    top: 28px;
    font-family: "Cabin Sketch", "Comic Sans MS", cursive;
    font-weight: 400;
    color: #eceaf4;
    line-height: 1;
    letter-spacing: 3px;
  }
  .headline .line-1 { display: block; font-size: 62px; margin-left: -10px; }
  .headline .line-2 { display: block; font-size: 62px; margin-top: 20px; margin-left: -10px; }
  .copy { position: absolute; left: 84px; right: 84px; font-size: 18.5px; line-height: 20px; }
  .intro { top: 258px; font-size: 20.5px; line-height: 19px; }
  .only-title { top: 336px; font-size: 20.5px; }
  .only-list { top: 374px; }
  .stat {
    top: 500px;
    left: 40px;
    right: 40px;
    font-family: "Cabin Sketch", "Comic Sans MS", cursive;
    font-size: 32px;
    line-height: 40px;
    letter-spacing: 1px;
    color: #eceaf4;
  }
  .stat strong { font-family: "Zilla Slab", Georgia, serif; font-weight: 600; font-size: 38px; }
  .successes-title { top: 578px; }
  .successes { top: 618px; }
  .means-title { top: 778px; }
  .means { top: 818px; }
  .partnership { top: 978px; }
  .future { top: 1058px; left: 70px; right: 70px; }
  .future .closing { font-size: 16px; }
</style>
</head>
<body>
<main class="poster">
  <div class="sky" role="img" aria-label="Blue and lilac sky with soft clouds rising from the lower right"></div>

  <div class="brand">
    <div class="brand-square"></div>
    <div class="brand-name">NORTHVALE PROBATION TRUST</div>
  </div>

  <div class="balloons" role="img" aria-label="Bunch of blue and pink celebration balloons"></div>

  <h1 class="headline">
    <span class="line-1">WE’RE</span>
    <span class="line-2">EXCEPTIONAL!</span>
  </h1>

  <p class="copy intro">Ashbrook Probation finished 2012-13 as an exceptionally performing district within<br>Northvale Probation Trust</p>

  <p class="copy only-title">Only district to:</p>
  <p class="copy only-list">Deliver sustained performance for over two years<br>Achieve the highest % rating two consecutive years<br>Achieve exceptional in all five critical measures – offender accommodation, employment, quality of RAPs and successful completion of orders/licences</p>

  <p class="copy stat">WE REDUCED RE OFFENDING BY <strong>9%</strong></p>

  <p class="copy successes-title">Our successes include:</p>
  <p class="copy successes">80% of offenders are successfull in completing their orders and licences. We supervised over 1,800 such sentences<br>When offenders on community orders failed to comply with the court order, we breached 97% of these offenders<br>When offenders failed to comply to protect the public we recalled 99% of these offenders</p>

  <p class="copy means-title">It means:</p>
  <p class="copy means">Our courts can have confidence in punishment in the community<br>Offenders are constructively managed with high quality interventions<br>Our communities can feel safer with the knowledge that we’re reducing crime</p>

  <p class="copy partnership">We’re proud to be a key player in the local community safety partnership where we make a visibly constructive contribution<br>It doesn’t end there…</p>

  <p class="copy future">We continue to lead towards becoming a market leader in offender assessment and offender management.<br><span class="closing">Our success means fewer victims and safer and stronger communities.</span></p>
</main>
</body>
</html>
```